New, modern business card for growing audiology practice

We need a new business card for our audiology practice. Our logo and website have recently changed (more modern) and we want our business cards to reflect this change.
We conduct hearing tests, perform earwax removals, and fit & dispense hearing aids to our patients. We are a family owned practice in which the owner is the one who works directly with the patient. I have attached logos in various formats to use, as well as two ideas I found on this website; as well as a scanned copy of our current logo. Good luck!

Industry/Entity Type

Business

Contact Information for Business Card

Company name: Maplow Hearing Center
Provider name: Peter Mulvoy, Au.D. F/ISN
Phone number: (555) 318-6042
Address: 87 W. Linden Ave. Harlow Falls, OH 45871
email: maplowhearing@postvale.net
website: maplowhearing.com

Colors
000000
aaaaaa
dbdbdb
cacaca
9bcb3c
afd23c
cadf82
b1b1b1

Requirements
Must have
• My card must include information in the "details" section. In the attached images, I found a few that I liked and I would like to model after - "brisk tumblin'" and "Sound Wellness Center".
• Must be horizontal.
• Must include logos provided. I uploaded them in various file formats and various ways.
• Must match logo font, if possible, if not, please get as close as you can.
Nice to have
• I really like the idea of having a color on one side with just the logo and company name and the contact information and provider name on the other side. I also really like the idea of having the main color dominating on the logo/company side with accent of that same color on the contact side of the card.
Should not have
• Must not be vertical.

```html
<!DOCTYPE html>
<html lang="en">
<head>
<meta charset="utf-8">
<title>Maplow Hearing Center – Business Card</title>
<link href="https://fonts.googleapis.com/css2?family=Lato:wght@400;700&display=swap" rel="stylesheet">
<style>
  :root {
    --backdrop: #e4e4e4;
    --green: #7aa83a;
    --green-light: #8bbb45;
    --green-dark: #62902e;
    --accent: #9bcb3c;
    --ink: #111111;
    --text: #3a3a3a;
    --paper: #ffffff;
    --paper-shade: #dcdcdc;
    --stripe: #000000;
  }
  * { box-sizing: border-box; margin: 0; padding: 0; }
  html, body {
    width: 1200px; height: 900px; overflow: hidden;
    background: var(--backdrop);
    font-family: "Lato", Arial, sans-serif;
  }
  .canvas { position: relative; width: 1200px; height: 900px; }
  .card {
    position: absolute; left: 240px; width: 720px; height: 411px;
    border-radius: 24px; overflow: hidden;
    box-shadow: 0 6px 18px rgba(0,0,0,0.25);
  }
  /* Front: brand side */
  .card--front {
    top: 24px;
    background: radial-gradient(ellipse at 55% 25%, var(--green-light) 0%, var(--green) 55%, var(--green-dark) 100%);
  }
  .brand {
    position: absolute; display: flex; align-items: center; gap: 12px;
    font-weight: 700; text-transform: uppercase; white-space: nowrap;
    color: var(--ink); letter-spacing: 0.5px;
  }
  .brand__dot {
    width: 26px; height: 26px; border-radius: 50%;
    border: 3px solid currentColor;
  }
  .card--front .brand { left: 50%; top: 170px; transform: translateX(-50%); font-size: 30px; }
  .card--front .brand__dot { border-color: var(--paper); }
  .front__web {
    position: absolute; left: 0; right: 0; bottom: 34px; text-align: center;
    color: rgba(255,255,255,0.75); font-size: 14px; letter-spacing: 0.5px;
  }
  /* Back: contact side */
  .card--back {
    top: 465px;
    background: linear-gradient(160deg, var(--paper) 0%, #f3f3f3 50%, var(--paper-shade) 100%);
  }
  .card--back .brand { left: 44px; top: 208px; font-size: 22px; }
  .card--back .brand__dot { width: 20px; height: 20px; border-color: var(--accent); }
  .divider {
    position: absolute; left: 412px; top: 70px; width: 2px; height: 180px;
    background: var(--green);
  }
  .contact { position: absolute; left: 436px; top: 74px; color: var(--text); }
  .contact__name { font-size: 18px; font-weight: 700; color: var(--ink); letter-spacing: 0.5px; text-transform: uppercase; }
  .contact__title { font-size: 15px; color: var(--green); margin-top: 2px; }
  .contact__address { font-size: 15px; line-height: 1.3; margin-top: 14px; }
  .contact__list { list-style: none; margin-top: 12px; font-size: 15px; line-height: 1.5; }
  .contact__list li { display: flex; align-items: center; gap: 10px; }
  .contact__icon { width: 14px; height: 14px; fill: var(--green); flex: none; }
  .back__footer { position: absolute; left: 0; top: 0; width: 720px; height: 411px; }
  .back__web {
    position: absolute; right: 34px; bottom: 28px;
    color: rgba(255,255,255,0.8); font-size: 15px; letter-spacing: 0.5px;
  }
</style>
</head>
<body>
<main class="canvas">
  <section class="card card--front" aria-label="Card front">
    <div class="brand"><span class="brand__dot"></span>Maplow Hearing Center</div>
    <div class="front__web">www.maplowhearing.com</div>
  </section>

  <section class="card card--back" aria-label="Card back">
    <svg class="back__footer" viewBox="0 0 720 411" aria-hidden="true">
      <path d="M0 373 L338 373 C334 378 330 381 322 381 L0 381 Z" fill="var(--stripe)"/>
      <path d="M0 386 L336 386 C362 386 372 338 418 334 L720 334 L720 411 L0 411 Z" fill="var(--green)"/>
    </svg>
    <div class="brand"><span class="brand__dot"></span>Maplow Hearing Center</div>
    <div class="divider"></div>
    <div class="contact">
      <p class="contact__name">Peter Mulvoy</p>
      <p class="contact__title">Au.D. F/ISN</p>
      <p class="contact__address">87 W. Linden Ave.<br>Harlow Falls, OH 45871</p>
      <ul class="contact__list">
        <li>
          <svg class="contact__icon" viewBox="0 0 16 16" aria-hidden="true"><path d="M3.5 1 L6 1 L7 5 L5.2 6.3 C6 8 7.8 9.9 9.7 10.8 L11 9 L15 10 L15 12.5 C15 13.9 13.9 15 12.5 15 C6.2 15 1 9.8 1 3.5 C1 2.1 2.1 1 3.5 1 Z"/></svg>
          (555) 318-6042
        </li>
        <li>
          <svg class="contact__icon" viewBox="0 0 16 16" aria-hidden="true"><path d="M1 3 L15 3 L8 9 Z"/><path d="M1 4.5 L8 10.5 L15 4.5 L15 13 L1 13 Z"/></svg>
          maplowhearing@postvale.net
        </li>
      </ul>
    </div>
    <div class="back__web">www.maplowhearing.com</div>
  </section>
</main>
</body>
</html>
```